Design needed for an A5 Flyer and Newspaper Ad

We are looking for a designer who can create us two graphical files. One is a flyer and one is a newspaper ad. Both have the same content. They just have a different format. Both the flyer and the ad should be in an adobe format.

Size:
Flyer format: A5
Newspaper format: 16 cm x 8 cm

The attached file Advertisement_KWT.indd is an ad of us for a different topic. But there is our logo in it.
We want you to create an ad and the flyer for gold purchase. I addes a file of a flyer from a competitor (1036 x 733.jpg). It can be made similar if you like. The file you make must be adjustable.

What needs to be on it:
Our Logo (Velten Haager AG)
Our address: Lindenweg 7, 5312 Brenntal
Since 1922

Font styles to use
Sans Serif

```html
<!DOCTYPE html>
<html lang="de">
<head>
<meta charset="utf-8">
<title>Velten Haager AG – Gold und Silber</title>
<link rel="stylesheet" href="https://fonts.googleapis.com/css2?family=Cinzel:wght@600;700;800;900&family=Open+Sans:wght@400&display=swap">
<style>
  :root{
    --bg:#1e1e1e;
    --gold-dark:#a7843c;
    --gold-mid:#c9a95e;
    --gold-light:#e8cf8a;
    --cream:#efe6d6;
    --band:#b36c2a;
    --ink:#1c1c1c;
    --brand:#c8202a;
    --white:#ffffff;
  }
  *{margin:0;padding:0;box-sizing:border-box}
  html,body{width:1200px;height:895px;overflow:hidden;background:var(--bg)}
  .flyer{position:absolute;left:66px;top:63px;width:1074px;height:758px;overflow:hidden;background:var(--cream)}
  .panel-left{position:absolute;left:0;top:0;width:504px;height:758px;
    background:radial-gradient(ellipse at 10% 30%,var(--gold-light) 0%,var(--gold-mid) 35%,var(--gold-dark) 100%)}
  .divider{position:absolute;left:504px;top:0;width:14px;height:758px;
    background:linear-gradient(90deg,var(--gold-mid),#f3dfa4 20%,#f3dfa4 35%,var(--gold-dark) 50%,var(--gold-light) 70%,#f6e7bd)}
  .panel-right{position:absolute;left:518px;top:0;width:556px;height:758px;
    background:linear-gradient(180deg,#f3d9a6 0%,#f1ebe2 22%,#ece6e0 70%,#e9c99a 100%)}
  .header-shape{position:absolute;left:0;top:0;width:520px;height:230px}
  .brand{position:absolute;left:40px;top:52px;width:380px;display:flex;align-items:center;gap:12px;
    font-family:'Cinzel',serif;font-weight:800;font-size:30px;color:var(--brand);letter-spacing:1px}
  .brand-dot{width:22px;height:22px;border-radius:50%;background:var(--brand);flex:none}
  .headline{position:absolute;left:0;width:504px;text-align:center;font-family:'Cinzel',serif;line-height:1}
  .headline-white{top:274px;font-size:54px;font-weight:800;color:var(--white);line-height:49px;
    text-shadow:2px 2px 2px rgba(60,40,10,.55)}
  .headline-white span{display:block}
  .word-gold{top:384px;font-size:96px;font-weight:900;
    background:linear-gradient(180deg,#f4dca0 0%,#c8973f 45%,#8e5f1e 60%,#e6c27a 100%);
    -webkit-background-clip:text;background-clip:text;color:transparent;
    filter:drop-shadow(2px 3px 2px rgba(70,45,10,.55))}
  .word-und{top:472px;font-size:38px;font-weight:900;color:var(--white);
    text-shadow:2px 2px 2px rgba(30,20,10,.8)}
  .word-silber{top:503px;font-size:96px;font-weight:900;
    background:linear-gradient(180deg,#ffffff 0%,#b7bcc1 40%,#4f565d 62%,#d0d4d8 100%);
    -webkit-background-clip:text;background-clip:text;color:transparent;
    filter:drop-shadow(2px 3px 2px rgba(30,30,30,.6))}
  .since{top:602px;font-size:24px;font-weight:700;color:var(--white);letter-spacing:3px;
    text-shadow:1px 1px 2px rgba(60,40,10,.6)}
  .jewellery{position:absolute;left:551px;top:99px;width:491px;height:300px;border-radius:50% 45% 40% 40%/45% 40% 55% 55%;
    background:radial-gradient(ellipse at 55% 55%,#e8b94a 0%,#c58d2a 45%,#a06b1c 75%,rgba(160,107,28,0) 100%)}
  .claim{position:absolute;left:518px;width:556px;text-align:center;font-family:'Cinzel',serif;color:var(--ink)}
  .claim-main{top:490px;font-size:33px;font-weight:800;line-height:38px}
  .claim-list{top:601px;font-size:18.5px;font-weight:700;line-height:22px}
  .footer-band{position:absolute;left:0;top:687px;width:1074px;height:42px;background:var(--band);
    font-family:'Open Sans',sans-serif;font-size:23px;color:var(--white)}
  .footer-web{position:absolute;left:0;width:504px;top:5px;text-align:center}
  .footer-address{position:absolute;left:603px;top:4px;display:flex;align-items:center;gap:12px}
  .footer-address svg{width:30px;height:30px}
</style>
</head>
<body>
<div class="flyer">
  <div class="panel-left"></div>
  <div class="divider"></div>
  <div class="panel-right"></div>

  <svg class="header-shape" viewBox="0 0 520 230" aria-hidden="true">
    <path d="M0 140 C110 198 250 214 310 202 C240 208 120 190 0 150 Z" fill="#f6ecd0"/>
    <path d="M0 0 H440 C500 25 480 155 330 182 C220 200 90 172 0 128 Z" fill="#ffffff"/>
  </svg>
  <div class="brand"><span class="brand-dot"></span>Velten Haager AG</div>

  <div class="headline headline-white"><span>Wir suchen</span><span>und kaufen</span></div>
  <div class="headline word-gold">Gold</div>
  <div class="headline word-und">und</div>
  <div class="headline word-silber">Silber</div>
  <div class="headline since">Seit 1922</div>

  <div class="jewellery" role="img" aria-label="Foto: Haufen aus Goldschmuck, Ringen, Ketten und Goldmünzen"></div>

  <div class="claim claim-main">Wir bezahlen mehr für<br>Goldvreneli als Ihre Bank!</div>
  <div class="claim claim-list">Goldvreneli, Altgold und Silber, Münzen,<br>Barren, Medaillen, Uhren, Ringe, Ketten</div>

  <div class="footer-band">
    <div class="footer-web">www.velten-haager.ch</div>
    <div class="footer-address">
      <svg viewBox="0 0 30 30" aria-hidden="true">
        <circle cx="15" cy="15" r="13.5" fill="none" stroke="#fff" stroke-width="2"/>
        <path d="M15 24 C11 19 9.5 16 9.5 13 A5.5 5.5 0 0 1 20.5 13 C20.5 16 19 19 15 24 Z" fill="none" stroke="#fff" stroke-width="2"/>
        <circle cx="15" cy="13" r="2" fill="#fff"/>
      </svg>
      <span>Lindenweg 7, 5312 Brenntal</span>
    </div>
  </div>
</div>
</body>
</html>
```